IT Product Event Invitations

We are requesting the design of two invitations for a series of technological events that will be held between the company Velto Grid and its partner in the Dominican Republic, Corvanel.
Both events represent the launch of the Velto Grid brand in the Dominican Republic.
The first event is an elegant dinner aimed at the banking sector of the Dominican Republic to showcase the "Ledgerwise Suite" software.
Event information:
- Descriptive text for the invitation: Corvanel y Velto Grid le invitan a descubrir cómo reducir costos, aumentar la automatización y mejorar la satisfacción de los clientes a través de una solución única para enfrentar los desafíos de la banca.
- Date: 25 de Septiembre
- Time: 7PM
- Location: El Miradero, Av. Tomás Herrandez 817
In the invitation, consider using the colors of the Velto Grid and Corvanel brands if possible. You can find the logos in the webpage
The second event is a wine tasting to present "Orbital Desk Platform" aimed at various industries.
Event information:
- Descriptive text for the invitation: Corvanel y Velto Grid le invitan a conocer una solución que le permitirá a toda su empresa brindar una experiencia de servicio a otro nivel.
- Date: 26 de Septiembre
- Time: 7PM
In the invitation, consider using the colors of the Velto Grid and Corvanel brands if possible. You can find the logos in the web page.
Both invitations must have a button for participant registration and that when you click on the image, it will direct you to a form.
Form for Ledgerwise Suite: https://signup.quilvane.example/events/a7Kq2Rm9Xw4Tz1Lp8Vb3Nc6Hd0Jf5Gs
Form for Orbital Desk Platform: https://signup.quilvane.example/events/b3Wd8Yt1Pq6Rn4Ks0Mz7Fc2Lx9Hv5Je

```html
<!DOCTYPE html>
<html lang="es">
<head>
<meta charset="utf-8">
<title>Invitaciones Velto Grid · Corvanel</title>
<link href="https://fonts.googleapis.com/css2?family=Bebas+Neue&family=Libre+Baskerville:wght@700&family=Mrs+Saint+Delafield&family=Poppins:wght@400;600;700&display=swap" rel="stylesheet">
<style>
  :root{
    --canvas:#cdcdcd;
    --paper:#f3f3f3;
    --green:#58bf46;
    --ink:#161616;
    --white:#ffffff;
    --orange:#f9aa4f;
    --red:#d3242f;
    --pill-line:#e0505a;
  }
  *{margin:0;padding:0;box-sizing:border-box}
  html,body{width:1200px;height:1200px;overflow:hidden;background:var(--canvas)}
  body{position:relative;font-family:"Poppins",sans-serif;color:var(--ink)}

  .flyer{position:absolute;top:237px;width:525px;height:677px;background:var(--paper);
    box-shadow:0 2px 8px rgba(0,0,0,.18);overflow:hidden}
  .flyer--dinner{left:45px}
  .flyer--wine{left:608px}

  .corner-band{position:absolute;left:0;top:0;width:153px;height:45px;background:var(--green)}
  .art-panel{position:absolute;left:0;top:53px;width:153px;height:427px;
    background:linear-gradient(180deg,var(--orange) 0%,#ec6d3e 50%,var(--red) 100%)}

  .event-type{position:absolute;left:171px;font-family:"Libre Baskerville",serif;font-weight:700;
    font-size:22px;letter-spacing:.5px;line-height:1}
  .event-sub{position:absolute;left:171px;top:90px;font-size:10px;line-height:12.5px;width:240px}

  .presents{position:absolute;left:171px;top:127px;width:311px;display:flex;align-items:center;
    gap:8px;font-size:11px;letter-spacing:3.2px}
  .presents::after{content:"";flex:1;height:1px;background:#b8b8b8}

  .title-main{position:absolute;left:171px;top:152px;font-family:"Libre Baskerville",serif;font-weight:700;
    color:var(--green);font-size:40px;line-height:1;letter-spacing:-.5px}
  .title-second{position:absolute;left:170px;top:194px;font-family:"Libre Baskerville",serif;font-weight:700;
    font-size:33px;line-height:1;letter-spacing:-.3px}
  .title-script{position:absolute;font-family:"Mrs Saint Delafield",cursive;line-height:1;color:var(--ink);white-space:nowrap}
  .audience{position:absolute;left:404px;top:250px;font-family:"Libre Baskerville",serif;font-weight:700;
    font-size:8px;line-height:9px;padding-left:5px;border-left:1px solid var(--ink)}
  .audience small{display:block;font-size:5px;font-weight:400;letter-spacing:.6px;margin-bottom:3px}

  .title-rule{position:absolute;left:171px;top:289px;width:300px;height:1px;background:var(--ink)}

  .intro{position:absolute;left:171px;top:308px;width:305px;font-size:9.8px;line-height:12.4px}

  .date-num{position:absolute;left:104px;top:368px;font-family:"Bebas Neue",sans-serif;font-size:142px;
    line-height:1;letter-spacing:-2px}
  .date-num .lead{color:var(--white);text-shadow:2px 2px 4px rgba(0,0,0,.25)}
  .date-de{position:absolute;left:227px;top:376px;font-family:"Bebas Neue",sans-serif;font-size:55px;line-height:1}
  .date-month{position:absolute;left:227px;top:422px;font-size:29px;line-height:1}
  .time-tag{position:absolute;left:230px;top:456px;width:167px;height:26px;background:var(--green);
    color:var(--white);font-weight:600;font-size:19px;letter-spacing:3.2px;line-height:26px;text-align:center}

  .venue{position:absolute;left:106px;top:504px;width:367px;height:30px}
  .venue-bar{position:absolute;left:16px;top:0;right:0;height:30px;background:var(--ink);color:var(--white);
    font-size:16.5px;line-height:30px;padding-left:17px;white-space:nowrap}
  .venue-pin{position:absolute;left:0;top:-1px;width:24px;height:32px}

  .partners{position:absolute;left:108px;top:558px;width:290px;height:26px;display:flex;align-items:center;gap:26px}
  .partner{display:flex;align-items:center;gap:6px;font-weight:700;color:var(--ink);white-space:nowrap}
  .partner--corvanel{font-size:15px}
  .partner--corvanel::before{content:"";width:14px;height:14px;border-radius:50%;background:var(--red)}
  .partner--velto{font-size:22px;letter-spacing:-.3px}

  .booking{position:absolute;left:110px;top:600px;width:364px;height:24px;border:1px solid var(--pill-line);
    border-radius:12px;display:flex;align-items:center;text-decoration:none;color:var(--ink);background:var(--paper);overflow:hidden}
  .booking-btn{flex:0 0 105px;height:24px;margin-left:-1px;border-radius:12px;white-space:nowrap;
    background:linear-gradient(90deg,#e0323a,#f79a3c);color:var(--white);font-size:12.5px;line-height:24px;text-align:center}
  .booking-url{padding-left:16px;font-size:14.5px;letter-spacing:1.6px;white-space:nowrap}
</style>
</head>
<body>

<article class="flyer flyer--dinner">
  <div class="corner-band"></div>
  <div class="art-panel" role="img" aria-label="Panel de patrón geométrico en chevrones sobre degradado naranja a rojo"></div>

  <h2 class="event-type" style="top:63px">DINNER</h2>
  <p class="event-sub">Aimed at the banking sector of the Dominican Republic to showcase</p>
  <p class="presents">PRESENTS</p>

  <h1 class="title-main">LEDGERWISE</h1>
  <p class="title-script" style="left:172px;top:202px;font-size:62px">Suite</p>
  <div class="title-rule"></div>

  <p class="intro">Corvanel y Velto Grid le invitan a descubrir cómo reducir costos, aumentar la automatización y mejorar la satisfacción de los clientes a través de una solución única para enfrentar los desafíos de la banca.</p>

  <p class="date-num"><span class="lead">2</span>5</p>
  <p class="date-de">DE</p>
  <p class="date-month">Septiembre</p>
  <p class="time-tag">Time: 7PM</p>

  <div class="venue">
    <div class="venue-bar">El Miradero, Av. Tomás Herrandez 817</div>
    <svg class="venue-pin" viewBox="0 0 24 32" aria-hidden="true"><path d="M12 1C5.9 1 1 5.8 1 11.8 1 19.5 12 31 12 31s11-11.5 11-19.2C23 5.8 18.1 1 12 1z" fill="#d3242f" stroke="#fff" stroke-width="1.5"/><circle cx="12" cy="11.5" r="4" fill="#fff"/></svg>
  </div>

  <div class="partners">
    <span class="partner partner--corvanel">Corvanel</span>
    <span class="partner partner--velto">Velto Grid</span>
  </div>

  <a class="booking" href="https://signup.quilvane.example/events/a7Kq2Rm9Xw4Tz1Lp8Vb3Nc6Hd0Jf5Gs">
    <span class="booking-btn">BOOK NOW</span>
    <span class="booking-url">https://qvn.example/R7pQ2</span>
  </a>
</article>

<article class="flyer flyer--wine">
  <div class="corner-band"></div>
  <div class="art-panel" role="img" aria-label="Panel de patrón geométrico en chevrones sobre degradado naranja a rojo"></div>

  <h2 class="event-type" style="top:98px">WINE TASTING</h2>
  <p class="presents">PRESENTS</p>

  <h1 class="title-main" style="font-size:43px">ORBITAL</h1>
  <p class="title-second">DESK</p>
  <p class="title-script" style="left:166px;top:236px;font-size:54px">Platform</p>
  <p class="audience"><small>AIMED AT</small>VARIOUS<br>INDUSTRIES</p>
  <div class="title-rule"></div>

  <p class="intro">Corvanel y Velto Grid le invitan a conocer una solución que le permitirá a toda su empresa brindar una experiencia de servicio a otro nivel.</p>

  <p class="date-num"><span class="lead">2</span>6</p>
  <p class="date-de">DE</p>
  <p class="date-month">Septiembre</p>
  <p class="time-tag">Time: 7PM</p>

  <div class="venue">
    <div class="venue-bar">El Miradero, Av. Tomás Herrandez 817</div>
    <svg class="venue-pin" viewBox="0 0 24 32" aria-hidden="true"><path d="M12 1C5.9 1 1 5.8 1 11.8 1 19.5 12 31 12 31s11-11.5 11-19.2C23 5.8 18.1 1 12 1z" fill="#d3242f" stroke="#fff" stroke-width="1.5"/><circle cx="12" cy="11.5" r="4" fill="#fff"/></svg>
  </div>

  <div class="partners">
    <span class="partner partner--corvanel">Corvanel</span>
    <span class="partner partner--velto">Velto Grid</span>
  </div>

  <a class="booking" href="https://signup.quilvane.example/events/b3Wd8Yt1Pq6Rn4Ks0Mz7Fc2Lx9Hv5Je">
    <span class="booking-btn">BOOK NOW</span>
    <span class="booking-url">https://qvn.example/R7pQ2</span>
  </a>
</article>

</body>
</html>
```